Investment Business - Biz Card Design

Using the attached logo files, please create a superior business card design for Tarnwell Holdings.

The "back" of the card should feature the logo (either in colour, or white/black over a feature colour)

The "front" of the card should feature: name, email, and phone

The design should be minimal and clean.

Target Market(s)

Business owners who need our investment services.

Industry/Entity Type

Business

```html
<!DOCTYPE html>
<html lang="en">
<head>
<meta charset="utf-8">
<title>Tarnwell Holdings – Business Card</title>
<link rel="stylesheet" href="https://fonts.googleapis.com/css2?family=Questrial&display=swap">
<style>
  :root {
    --ink: #000000;
    --paper: #ffffff;
    --blue-deep: #2a55ff;
    --blue-mid: #93a9fb;
    --blue-pale: #f4f6ff;
    --accent-soft: rgba(246, 247, 253, 0.6);
    --accent-clear: rgba(246, 247, 253, 0);
    --font: "Questrial", sans-serif;
  }
  html, body {
    margin: 0;
    padding: 0;
    width: 1050px;
    height: 1200px;
    overflow: hidden;
    background: var(--paper);
    font-family: var(--font);
  }
  .canvas {
    position: relative;
    width: 1050px;
    height: 1200px;
  }
  .card {
    position: absolute;
    box-sizing: border-box;
    border: 2px solid var(--ink);
    border-radius: 64px;
    overflow: hidden;
  }
  .card--front {
    left: 7px;
    top: 4px;
    width: 1038px;
    height: 578px;
    background: linear-gradient(150deg, var(--blue-pale) 0%, var(--blue-mid) 55%, var(--blue-deep) 100%);
  }
  .card--back {
    left: 3px;
    top: 618px;
    width: 1038px;
    height: 576px;
    background: linear-gradient(150deg, var(--blue-deep) 0%, var(--blue-mid) 40%, var(--blue-pale) 100%);
  }
  .accent-area {
    position: absolute;
    left: 430px;
    top: 0;
    width: 606px;
    height: 100%;
    background: linear-gradient(120deg, var(--accent-clear) 10%, var(--accent-soft) 50%, var(--accent-clear) 90%);
  }
  .front-name {
    position: absolute;
    left: 50px;
    top: 52px;
    margin: 0;
    font-size: 64px;
    font-weight: 400;
    letter-spacing: 2px;
    color: var(--ink);
  }
  .contact {
    position: absolute;
    left: 36px;
    top: 300px;
    margin: 0;
    display: grid;
    grid-template-columns: 212px auto;
    row-gap: 16px;
    font-size: 32px;
    color: var(--ink);
  }
  .contact dt, .contact dd { margin: 0; line-height: 36px; }
  .wordmark {
    position: absolute;
    margin: 0;
    font-weight: 400;
    text-align: center;
    line-height: 1;
  }
  .wordmark__main {
    display: block;
    letter-spacing: 3px;
  }
  .wordmark__sub {
    display: block;
    letter-spacing: 14px;
    margin-top: 6px;
  }
  .wordmark--front {
    right: 42px;
    bottom: 30px;
    color: var(--ink);
  }
  .wordmark--front .wordmark__main { font-size: 56px; }
  .wordmark--front .wordmark__sub { font-size: 20px; }
  .wordmark--back-top {
    left: 34px;
    top: 40px;
    color: var(--paper);
  }
  .wordmark--back-top .wordmark__main { font-size: 76px; }
  .wordmark--back-top .wordmark__sub { font-size: 26px; letter-spacing: 18px; }
  .wordmark--back-bottom {
    right: 40px;
    bottom: 26px;
    color: var(--ink);
  }
  .wordmark--back-bottom .wordmark__main { font-size: 76px; }
  .wordmark--back-bottom .wordmark__sub { font-size: 26px; letter-spacing: 18px; }
</style>
</head>
<body>
<main class="canvas">
  <section class="card card--front" aria-label="Card front">
    <div class="accent-area" role="img" aria-label="Decorative sweeping ribbon accent in pale blue and white"></div>
    <p class="front-name">TARNWELL</p>
    <dl class="contact">
      <dt>NAME</dt><dd>:</dd>
      <dt>EMAIL</dt><dd>:</dd>
      <dt>PHONE</dt><dd>:</dd>
    </dl>
    <p class="wordmark wordmark--front">
      <span class="wordmark__main">TARNWELL</span>
      <span class="wordmark__sub">HOLDINGS</span>
    </p>
  </section>

  <section class="card card--back" aria-label="Card back">
    <p class="wordmark wordmark--back-top">
      <span class="wordmark__main">TARNWELL</span>
      <span class="wordmark__sub">HOLDINGS</span>
    </p>
    <p class="wordmark wordmark--back-bottom">
      <span class="wordmark__main">TARNWELL</span>
      <span class="wordmark__sub">HOLDINGS</span>
    </p>
  </section>
</main>
</body>
</html>
```